Bimvoro Power Point Presentation

We need our presentation designed. Our current presentation is inconsistent, too text heavy, and complicated. We want this to be clean, sleek, and impressive as our references attached are.

Our colors are blue, black, and white.
Our font is roboto.

```html
<!DOCTYPE html>
<html lang="en">
<head>
<meta charset="utf-8">
<title>Bimvoro — Media Kit Presentation</title>
<link href="https://fonts.googleapis.com/css2?family=Roboto:wght@300;400;500;700&display=swap" rel="stylesheet">
<style>
:root{
  --blue:#1282f0;
  --blue-soft:#5aa9f8;
  --blue-pale:#8cc4fb;
  --ink:#1d232c;
  --footer-dark:#1f2632;
  --canvas:#d8d8d8;
  --bar:#eeeeee;
  --line:#e2e2e2;
  --white:#ffffff;
}
*{box-sizing:border-box;margin:0;padding:0}
html,body{width:1200px;height:2453px;overflow:hidden}
body{position:relative;background:var(--canvas);font-family:'Roboto',sans-serif;color:var(--ink)}
.abs{position:absolute}

/* brand lockup */
.brand{position:absolute;display:flex;align-items:center;gap:6px;font-weight:500;white-space:nowrap}
.brand .mark{display:block;background:currentColor}
.brand-top{left:30px;top:33px;color:var(--white);font-size:19px}
.brand-top .mark{width:22px;height:22px}

/* slide frame */
.slide{position:absolute;width:540px;height:303px;background:var(--white);overflow:hidden}
.photo{position:absolute}
.tone-shop{background:linear-gradient(135deg,#6f6456,#c8bba5 55%,#8f8474)}
.tone-screen{background:linear-gradient(135deg,#5e6b78,#aab6c0 50%,#4a5560)}
.tone-hall{background:linear-gradient(135deg,#9aa4ad,#e3e7ea 55%,#7b8894)}
.tone-food{background:linear-gradient(135deg,#5a3a22,#b9844f 55%,#3b2a1e)}
.tone-person{background:linear-gradient(135deg,#9b9b9b,#e0e0e0 50%,#b0303a)}
.tone-grocery{background:linear-gradient(135deg,#2f7a3a,#e39a3a 50%,#4b8b3f)}
.tone-map{background:linear-gradient(135deg,#e9edf2,#c4d2e1)}

/* cover */
.cover{background:var(--blue)}
.cover .side{position:absolute;left:305px;top:0;width:235px;height:281px;background:var(--white)}
.cover .photo{border:2px solid var(--white)}
.cover .brand{left:42px;top:47px;color:var(--white);font-size:22px;font-weight:400}
.cover .brand .mark{width:24px;height:24px}
.cover-title{position:absolute;left:42px;top:114px;color:var(--white);font-size:24.5px;font-weight:700;line-height:27px}
.cover-date{position:absolute;left:42px;top:181px;color:var(--white);font-size:6.5px}
.cover-btn{position:absolute;left:42px;top:226px;width:98px;height:15px;border-radius:3px;background:var(--blue-soft);color:var(--white);font-size:5.5px;font-weight:500;display:flex;align-items:center;justify-content:center;box-shadow:0 1px 2px rgba(0,0,0,.2)}
.slide-bar{position:absolute;left:0;bottom:0;width:100%;height:22px;background:var(--footer-dark);color:var(--white);font-size:5.5px;display:flex;align-items:center;justify-content:center}
.slide-bar span{color:var(--blue-soft)}
.hero{position:absolute;left:234px;top:112px;width:540px;height:303px;transform:scale(1.354,1.36);transform-origin:0 0}
.rounded .photo{border:5px solid var(--blue);border-radius:14px}

/* content slide chrome */
.head-mark{position:absolute;left:26px;top:25px;width:22px;height:22px;background:var(--blue)}
.head-title{position:absolute;left:60px;top:28px;font-size:19.5px;font-weight:500;color:var(--ink)}
.head-sub{position:absolute;left:60px;top:52px;font-size:12px;font-weight:300;color:var(--blue)}
.foot{position:absolute;left:0;bottom:0;width:100%;height:30px}
.foot .brand{left:16px;top:5px;color:var(--blue);font-size:12.5px}
.foot .brand .mark{width:14px;height:14px}
.foot .track{position:absolute;left:98px;top:10px;width:410px;height:9px;background:var(--bar)}
.foot .page{position:absolute;left:500px;top:9px;width:18px;height:12px;border-radius:3px;background:var(--blue);color:var(--white);font-size:6px;font-weight:700;display:flex;align-items:center;justify-content:center}

/* why indoor */
.why-col{position:absolute;top:0;height:303px;text-align:center;color:var(--white)}
.why-col h4{font-size:9.5px;font-weight:500;margin-top:20px}
.why-col .item{position:absolute;left:0;width:100%}
.why-col .dot{width:26px;height:26px;border-radius:50%;margin:0 auto;display:flex;align-items:center;justify-content:center}
.why-col p{font-size:5.3px;line-height:6px;margin-top:3px;padding:0 12px}

/* statement slide */
.wash{background:linear-gradient(180deg,rgba(18,130,240,.86),rgba(18,130,240,.9)),linear-gradient(90deg,#6c7884,#c9d2d9 60%,#56616c)}
.statement{position:absolute;left:40px;right:40px;top:137px;text-align:center;color:var(--white);font-size:16.3px;font-weight:300;line-height:19.5px}

/* advertisers */
.brand-band{position:absolute;left:0;top:103px;width:540px;height:132px;background:var(--blue)}
.tile{position:absolute;width:55px;height:45px;background:var(--white);border-radius:8px;display:flex;align-items:center;justify-content:center;font-size:8px;font-weight:700;color:var(--ink);box-shadow:0 2px 3px rgba(0,0,0,.15)}

/* takeaways */
.lead{position:absolute;left:40px;top:93px;font-size:11.5px;color:var(--blue);font-weight:300}
.ticks{position:absolute;left:38px;top:122px;width:245px;list-style:none}
.ticks li{position:relative;padding-left:20px;font-size:7.3px;line-height:8.2px;margin-bottom:8.5px}
.ticks li::before{content:"✓";position:absolute;left:0;top:0;color:var(--blue);font-size:7px}
.claim{position:absolute;left:295px;top:40px;width:221px;height:193px;background:var(--blue);border-radius:40px 20px 40px 30px;color:var(--white);font-size:14.5px;font-weight:500;line-height:22px;display:flex;align-items:center;justify-content:center;text-align:center}

/* formats table */
.spec{position:absolute;left:26px;top:93px;width:489px;border-collapse:collapse;font-size:5.8px}
.spec th{height:23px;text-align:left;padding-left:4px;color:var(--white);font-size:8.5px;font-weight:500}
.spec th.c1{background:var(--blue)} .spec th.c2{background:var(--ink)} .spec th.c3{background:var(--blue-pale)}
.spec td{height:25px;border:1px solid var(--line);padding-left:4px;vertical-align:middle;line-height:7px}
.spec td::before{content:"✓ ";color:var(--blue)}
.spec td.empty::before{content:""}

/* how to buy */
.buy-grid{position:absolute;left:25px;top:92px;width:490px;height:165px;border:1px solid var(--line)}
.buy-row{position:absolute;left:0;width:100%;border-bottom:1px solid var(--line)}
.buy-label{position:absolute;left:12px;font-size:12px;line-height:13px;color:var(--ink)}
.buy-cell{position:absolute;height:40px;border:1px solid var(--line);display:flex;align-items:center;gap:8px;padding-left:10px;font-size:7.5px;line-height:8px}
.buy-cell svg{flex:none}
.partner{position:absolute;font-size:8.5px;font-weight:500;color:var(--ink)}

/* network */
.panel{position:absolute;top:97px;width:240px;height:153px;border:1px solid var(--line)}
.panel h5{position:absolute;left:10px;top:10px;font-size:12px;font-weight:400}
.panel h5 b{color:var(--blue);font-weight:500}
.stat{position:absolute;top:43px;width:53px;height:44px;border-radius:6px;background:var(--blue);color:var(--white);text-align:center;padding-top:6px}
.stat strong{display:block;font-size:11.5px;font-weight:500}
.stat small{display:block;font-size:4.8px;line-height:5px;margin-top:3px}

/* thank you */
.thanks-title{position:absolute;left:58px;top:188px;color:var(--white);font-size:23px;font-weight:700}
.thanks-sub{position:absolute;left:58px;top:222px;color:var(--white);font-size:10px;font-weight:300}
</style>
</head>
<body>

<div class="brand brand-top"><span class="mark"></span>Bimvoro</div>

<!-- hero cover -->
<div class="hero">
  <div class="slide cover">
    <div class="side"></div>
    <div class="photo tone-shop" style="left:290px;top:8px;width:100px;height:82px" role="img" aria-label="Pharmacy aisle with ceiling mounted screen"></div>
    <div class="photo tone-screen" style="left:398px;top:8px;width:138px;height:82px" role="img" aria-label="Row of screens above a counter"></div>
    <div class="photo tone-hall" style="left:290px;top:98px;width:160px;height:88px" role="img" aria-label="Man walking past a digital kiosk"></div>
    <div class="photo tone-food" style="left:458px;top:98px;width:78px;height:88px" role="img" aria-label="Restaurant bar with screens"></div>
    <div class="photo tone-person" style="left:290px;top:194px;width:100px;height:86px" role="img" aria-label="Customer viewing a wall screen"></div>
    <div class="photo tone-grocery" style="left:398px;top:194px;width:138px;height:86px" role="img" aria-label="Grocery store with digital coupon signage"></div>
    <div class="brand"><span class="mark"></span>Bimvoro</div>
    <div class="cover-title">Indoor DOOH<br>Audiences at Scale</div>
    <div class="cover-date">Wednesday, December 1, 2021</div>
    <div class="cover-btn">BUY ON BIMVORO</div>
    <div class="slide-bar">info@<span>bimvoro</span>.com&nbsp;|&nbsp;<span>MEDIA KIT</span>&nbsp;2021</div>
  </div>
</div>

<!-- row 1 -->
<div class="slide cover" style="left:50px;top:803px">
  <div class="side"></div>
  <div class="photo tone-shop" style="left:290px;top:8px;width:84px;height:82px" role="img" aria-label="Pharmacy aisle with ceiling mounted screen"></div>
  <div class="photo tone-screen" style="left:380px;top:8px;width:160px;height:82px" role="img" aria-label="Row of screens above a counter"></div>
  <div class="photo tone-hall" style="left:290px;top:96px;width:160px;height:86px" role="img" aria-label="Man walking past a digital kiosk"></div>
  <div class="photo tone-food" style="left:456px;top:96px;width:84px;height:86px" role="img" aria-label="Restaurant bar with screens"></div>
  <div class="photo tone-person" style="left:290px;top:188px;width:84px;height:93px" role="img" aria-label="Customer viewing a wall screen"></div>
  <div class="photo tone-grocery" style="left:380px;top:188px;width:160px;height:93px" role="img" aria-label="Grocery store with digital coupon signage"></div>
  <div class="brand"><span class="mark"></span>Bimvoro</div>
  <div class="cover-title">Indoor DOOH<br>Audiences at Scale</div>
  <div class="cover-date">Wednesday, December 1, 2021</div>
  <div class="cover-btn">BUY ON BIMVORO</div>
  <div class="slide-bar">info@<span>bimvoro</span>.com&nbsp;|&nbsp;<span>MEDIA KIT</span>&nbsp;2021</div>
</div>

<div class="slide cover rounded" style="left:608px;top:803px">
  <div class="side"></div>
  <div class="photo tone-person" style="left:287px;top:14px;width:90px;height:72px" role="img" aria-label="Customer viewing a wall screen"></div>
  <div class="photo tone-food" style="left:385px;top:12px;width:145px;height:118px" role="img" aria-label="Restaurant bar with screens"></div>
  <div class="photo tone-screen" style="left:287px;top:96px;width:90px;height:72px" role="img" aria-label="Clinic hallway screen"></div>
  <div class="photo tone-grocery" style="left:385px;top:140px;width:145px;height:118px" role="img" aria-label="Grocery store with digital coupon signage"></div>
  <div class="photo tone-hall" style="left:287px;top:178px;width:90px;height:78px" role="img" aria-label="Man walking past a digital kiosk"></div>
  <div class="brand"><span class="mark"></span>Bimvoro</div>
  <div class="cover-title">Indoor DOOH<br>Audiences at Scale</div>
  <div class="cover-date">Wednesday, December 1, 2021</div>
  <div class="cover-btn">BUY ON BIMVORO</div>
  <div class="slide-bar">info@<span>bimvoro</span>.com&nbsp;|&nbsp;<span>MEDIA KIT</span>&nbsp;2021</div>
</div>

<!-- row 2 -->
<div class="slide" style="left:50px;top:1125px">
  <div class="abs" style="left:122px;top:78px;width:22px;height:22px;background:var(--blue)"></div>
  <div class="abs" style="left:0;top:112px;width:270px;text-align:center;font-size:19.5px;font-weight:500">Why Go Indoor</div>
  <div class="abs" style="left:38px;top:147px;width:194px;text-align:center;font-size:9.5px;line-height:12px;font-weight:300;color:var(--blue)">it's not just lockdowns ending - recent uptick has been driven by the unique effectiveness of indoor DOOH ad exposure.</div>

  <div class="why-col" style="left:270px;width:135px;background:var(--blue)">
    <h4>It's special...</h4>
    <div class="item" style="top:48px"><div class="dot" style="background:var(--ink)"><svg width="14" height="9" viewBox="0 0 14 9"><ellipse cx="7" cy="4.5" rx="6.5" ry="4" fill="#fff"/><circle cx="7" cy="4.5" r="2" fill="#1d232c"/></svg></div><p>Dwell time measured in minutes, not seconds</p></div>
    <div class="item" style="top:102px"><div class="dot" style="background:var(--ink);color:#fff;font-size:12px;font-weight:700">$</div><p>Brand-safe</p></div>
    <div class="item" style="top:156px"><div class="dot" style="background:var(--ink)"><svg width="12" height="12" viewBox="0 0 12 12"><circle cx="6" cy="3.5" r="2.6" fill="#fff"/><path d="M1 12c0-3.5 2.2-5 5-5s5 1.5 5 5z" fill="#fff"/></svg></div><p>100% viewability by humans, not bots</p></div>
    <div class="item" style="top:210px"><div class="dot" style="background:var(--ink)"><svg width="12" height="12" viewBox="0 0 12 12"><rect x="1" y="1" width="10" height="10" rx="2" fill="none" stroke="#fff" stroke-width="1.5"/><circle cx="6" cy="6" r="2.3" fill="#fff"/></svg></div><p>Not<br>Skippable</p></div>
  </div>

  <div class="why-col" style="left:405px;width:135px;background:linear-gradient(160deg,#3a3f47,#16191e)" role="img" aria-label="Dark in-store screen backdrop">
    <h4>It's powerful...</h4>
    <div class="item" style="top:48px"><div class="dot" style="background:var(--blue)"><svg width="12" height="11" viewBox="0 0 12 11"><path d="M1 4h3l5-3v9L4 7H1z" fill="#fff"/></svg></div><p>Engaged impressions, consumer attention, means...</p></div>
    <div class="item" style="top:102px"><div class="dot" style="background:var(--blue)"><svg width="12" height="12" viewBox="0 0 12 12"><circle cx="6" cy="6" r="5" fill="none" stroke="#fff" stroke-width="1.2"/><circle cx="6" cy="6" r="2" fill="#fff"/></svg></div><p>...Indoor DOOH 2x more likely to be seen, recalled, than traditional OOH1</p></div>
    <div class="abs" style="left:0;top:178px;width:100%;font-size:9.5px;font-weight:500">And it works.</div>
    <div class="item" style="top:210px"><div class="dot" style="background:var(--blue)"><svg width="12" height="12" viewBox="0 0 12 12"><path d="M2 6a4 4 0 0 1 7-2.6M10 6a4 4 0 0 1-7 2.6" fill="none" stroke="#fff" stroke-width="1.4"/><path d="M9.5 1v3h-3M2.5 11V8h3" fill="none" stroke="#fff" stroke-width="1.2"/></svg></div><p>2x increase in reach if added to Omni-Channel campaigns2</p></div>
  </div>

  <div class="foot">
    <div class="brand"><span class="mark"></span>Bimvoro</div>
    <div class="track" style="width:220px"></div>
    <div class="page">3</div>
  </div>
</div>

<div class="slide wash" style="left:608px;top:1125px" role="img" aria-label="Digital kiosk in a transit concourse under blue wash">
  <div class="brand" style="left:216px;top:85px;color:var(--white);font-size:20px;font-weight:400"><span class="mark" style="width:20px;height:20px"></span>Bimvoro</div>
  <div class="statement">Bimvoro offers advertisers easy, affordable access to North America's largest indoor DOOH network, containing diverse audience segments while captivated in indoor environments</div>
</div>

<!-- row 3 -->
<div class="slide" style="left:50px;top:1447px">
  <div class="head-mark"></div>
  <div class="head-title">Advertisers</div>
  <div class="head-sub">Brands that buy on our network.</div>
  <div class="brand-band">
    <div class="tile" style="left:23px;top:10px">Corvelle</div>
    <div class="tile" style="left:86px;top:10px">Brindle</div>
    <div class="tile" style="left:149px;top:10px">Puckline</div>
    <div class="tile" style="left:212px;top:10px">Tidewell</div>
    <div class="tile" style="left:275px;top:10px">Crumbo</div>
    <div class="tile" style="left:338px;top:10px">Lumora</div>
    <div class="tile" style="left:401px;top:10px">Vespre</div>
    <div class="tile" style="left:464px;top:10px">Halvard</div>
    <div class="tile" style="left:23px;top:73px">Norhem</div>
    <div class="tile" style="left:86px;top:73px">Pipcrunch</div>
    <div class="tile" style="left:149px;top:73px">Tempora</div>
    <div class="tile" style="left:212px;top:73px">Kiddoplay</div>
    <div class="tile" style="left:275px;top:73px">Fizzmoor</div>
    <div class="tile" style="left:338px;top:73px">Tunewave</div>
    <div class="tile" style="left:401px;top:73px">Keelbank</div>
    <div class="tile" style="left:464px;top:73px">Dashtly</div>
  </div>
  <div class="foot">
    <div class="brand"><span class="mark"></span>Bimvoro</div>
    <div class="track"></div>
    <div class="page">5</div>
  </div>
</div>

<div class="slide" style="left:608px;top:1447px">
  <div class="head-mark"></div>
  <div class="head-title">Key Takeaways</div>
  <div class="lead">Bimvoro is:</div>
  <ul class="ticks">
    <li>North America's largest and fastest-growing indoor DOOH screen network</li>
    <li>Powerful enough to capture the attention of nationwide audiences at scale, specific enough to provide access to diverse audience segments</li>
    <li>Programmatically-accessible, ensuring cost-efficiency, transparency and real-time optimizations</li>
    <li>Flexible enough to get any DOOH campaign or integration up and running quickly and without issue</li>
  </ul>
  <div class="claim">The Right Time.<br>The Right Message.<br>The Right Audience.</div>
  <div class="foot">
    <div class="brand"><span class="mark"></span>Bimvoro</div>
    <div class="track"></div>
    <div class="page">6</div>
  </div>
</div>

<!-- row 4 -->
<div class="slide" style="left:50px;top:1769px">
  <div class="head-mark"></div>
  <div class="head-title">Digital Media Formats</div>
  <div class="head-sub">Specifications</div>
  <table class="spec">
    <tr><th class="c1" style="width:162px">Network</th><th class="c2" style="width:163px">Content Specifications</th><th class="c3">Ad Content Play Suggestions</th></tr>
    <tr><td>Indoor, 32 –73" Screens</td><td>1920 pixels (w) x 1080 pixels (h) 16:9</td><td>15 second</td></tr>
    <tr><td>Full Screen Take Over</td><td>1080 pixels (w) x 1920 pixels (h) 9:16</td><td>30 second</td></tr>
    <tr><td>Sold programmatically</td><td>Static: PNG, RGB, encoded. JPG or H.264</td><td>60 second</td></tr>
    <tr><td>No Blacklisted Advertisers</td><td>Video: .MP$ / encoded .MOV</td><td class="empty"></td></tr>
    <tr><td>Approval Upon Venue Review</td><td>Will repurpose TV spots, banner ads; transcode ill-fitting static creatives</td><td class="empty"></td></tr>
  </table>
  <div class="foot">
    <div class="brand"><span class="mark"></span>Bimvoro</div>
    <div class="track"></div>
    <div class="page">7</div>
  </div>
</div>

<div class="slide" style="left:608px;top:1769px">
  <div class="head-mark"></div>
  <div class="head-title">How To Buy</div>
  <div class="head-sub" style="font-size:10px">Bimvoro's network and unique audiences are accessible however you buy your media.</div>
  <div class="buy-grid">
    <div class="buy-row" style="top:0;height:55px">
      <div class="buy-label" style="top:20px">Audiences...</div>
      <div class="buy-cell" style="left:122px;top:6px;width:116px"><svg width="22" height="20" viewBox="0 0 22 20"><circle cx="8" cy="5" r="3.5" fill="none" stroke="#1282f0" stroke-width="1.3"/><path d="M2 19c0-5 3-7 6-7s6 2 6 7" fill="none" stroke="#1282f0" stroke-width="1.3"/><circle cx="17" cy="13" r="4" fill="none" stroke="#1282f0" stroke-width="1.3"/></svg>High<br>Net Worth</div>
      <div class="buy-cell" style="left:246px;top:6px;width:116px"><svg width="22" height="18" viewBox="0 0 22 18"><rect x="1" y="1" width="20" height="16" fill="none" stroke="#1282f0" stroke-width="1.3"/><path d="M11 1v16" stroke="#1282f0" stroke-width="1.3"/><circle cx="11" cy="9" r="3" fill="none" stroke="#1282f0" stroke-width="1.3"/></svg>Sports<br>Fans</div>
      <div class="buy-cell" style="left:370px;top:6px;width:114px"><svg width="22" height="20" viewBox="0 0 22 20"><circle cx="7" cy="5" r="3.5" fill="none" stroke="#1282f0" stroke-width="1.3"/><path d="M1 19c0-5 3-7 6-7s6 2 6 7" fill="none" stroke="#1282f0" stroke-width="1.3"/><circle cx="17" cy="5" r="4" fill="none" stroke="#1282f0" stroke-width="1.3"/><path d="M17 3v2h2" fill="none" stroke="#1282f0" stroke-width="1.2"/></svg>High<br>Dwell Time</div>
    </div>
    <div class="buy-row" style="top:55px;height:60px">
      <div class="buy-label" style="top:18px">... you can buy<br><b style="font-weight:500">anywhere</b>...</div>
      <div class="partner" style="left:135px;top:14px">Ovanto</div>
      <div class="partner" style="left:200px;top:14px">Trekado</div>
      <div class="partner" style="left:275px;top:14px">Quantiv</div>
      <div class="partner" style="left:345px;top:10px;font-size:7px;line-height:7px">Veranta<br>media</div>
      <div class="partner" style="left:430px;top:14px">Skylot</div>
      <div class="partner" style="left:135px;top:36px">Astrel</div>
      <div class="partner" style="left:200px;top:36px">Bidcraft</div>
      <div class="partner" style="left:275px;top:36px">Combstack</div>
      <div class="partner" style="left:350px;top:36px">Beatpoint</div>
      <div class="partner" style="left:430px;top:36px">Fireside</div>
    </div>
    <div class="buy-row" style="top:115px;height:50px;border-bottom:0">
      <div class="buy-label" style="top:10px">...however<br><b style="font-weight:500">you'd like</b>.</div>
      <div class="buy-cell" style="left:122px;top:4px;width:116px"><svg width="20" height="20" viewBox="0 0 20 20"><path d="M3 10l6-7 8 8-7 6z" fill="none" stroke="#1282f0" stroke-width="1.3"/><circle cx="8" cy="9" r="1.5" fill="#1282f0"/></svg>Direct<br>Buying</div>
      <div class="buy-cell" style="left:246px;top:4px;width:116px"><svg width="20" height="20" viewBox="0 0 20 20"><circle cx="10" cy="10" r="2.5" fill="none" stroke="#1282f0" stroke-width="1.3"/><circle cx="3" cy="3" r="2" fill="none" stroke="#1282f0" stroke-width="1.2"/><circle cx="17" cy="3" r="2" fill="none" stroke="#1282f0" stroke-width="1.2"/><circle cx="3" cy="17" r="2" fill="none" stroke="#1282f0" stroke-width="1.2"/><circle cx="17" cy="17" r="2" fill="none" stroke="#1282f0" stroke-width="1.2"/><path d="M4.5 4.5l3.5 3.5M15.5 4.5L12 8M4.5 15.5L8 12M15.5 15.5L12 12" stroke="#1282f0" stroke-width="1.2"/></svg>Open<br>RTB</div>
      <div class="buy-cell" style="left:370px;top:4px;width:114px"><svg width="20" height="20" viewBox="0 0 20 20"><rect x="2" y="2" width="12" height="12" fill="none" stroke="#1282f0" stroke-width="1.3"/><rect x="7" y="7" width="11" height="11" fill="none" stroke="#1282f0" stroke-width="1.3"/></svg>Programmatic<br>Guaranteed<br>Or PMP</div>
    </div>
  </div>
  <div class="foot">
    <div class="brand"><span class="mark"></span>Bimvoro</div>
    <div class="track"></div>
    <div class="page">8</div>
  </div>
</div>

<!-- row 5 -->
<div class="slide" style="left:50px;top:2091px">
  <div class="head-mark"></div>
  <div class="head-title">Network</div>
  <div class="head-sub" style="font-size:10px;line-height:11px;width:450px">Bimvoro is your DOOH partner, connecting your partners and advertisers to a nation-wide network of premium, place-based screens.</div>
  <div class="panel" style="left:25px">
    <h5>Our <b>Nationwide</b> Network.</h5>
    <div class="stat" style="left:6px"><strong>12B+</strong><small>Impressions<br>Annually</small></div>
    <div class="stat" style="left:64px"><strong>50+</strong><small>DMA's</small></div>
    <div class="stat" style="left:122px"><strong>26,105+</strong><small>Venues</small></div>
    <div class="stat" style="left:180px"><strong>31,594+</strong><small>Screens</small></div>
    <div class="photo tone-map" style="left:14px;top:92px;width:100px;height:55px" role="img" aria-label="Map of United States venue locations"></div>
    <div class="photo tone-map" style="left:128px;top:92px;width:100px;height:55px" role="img" aria-label="Map of Canada venue locations"></div>
  </div>
  <div class="panel" style="left:275px">
    <h5>Our <b>Premium</b> Venue Types.</h5>
    <div class="stat" style="left:6px"><strong>12000+</strong><small>Retail<br>Screens</small></div>
    <div class="stat" style="left:64px"><strong>16000</strong><small>Restobar<br>Screens</small></div>
    <div class="stat" style="left:122px"><strong>2000+</strong><small>Medical<br>Screens</small></div>
    <div class="stat" style="left:180px"><strong>4000+</strong><small>Grocery<br>Screens</small></div>
    <div class="abs" style="left:10px;top:92px;font-size:5.3px">Plus private airports, hockey arenas, records stores, and many more.</div>
    <div class="photo tone-shop" style="left:6px;top:103px;width:73px;height:46px" role="img" aria-label="Pharmacy aisle with screen"></div>
    <div class="photo tone-food" style="left:83px;top:103px;width:73px;height:46px" role="img" aria-label="Restaurant bar with screens"></div>
    <div class="photo tone-hall" style="left:160px;top:103px;width:73px;height:46px" role="img" aria-label="Clinic waiting area with screen"></div>
  </div>
  <div class="foot">
    <div class="brand"><span class="mark"></span>Bimvoro</div>
    <div class="track"></div>
    <div class="page">9</div>
  </div>
</div>

<div class="slide wash" style="left:608px;top:2091px" role="img" aria-label="Digital kiosk in a transit concourse under blue wash">
  <div class="brand" style="left:58px;top:148px;color:var(--white);font-size:20px;font-weight:400"><span class="mark" style="width:20px;height:20px"></span>Bimvoro</div>
  <div class="thanks-title">Thank You!</div>
  <div class="thanks-sub">for your Time and Attention ...</div>
  <div class="slide-bar" style="height:18px">info@<span>bimvoro</span>.com&nbsp;|&nbsp;<span>MEDIA KIT</span>&nbsp;2021</div>
</div>

</body>
</html>
```